Business Card Design

Business card design.

Business card is to have logo, website address and email address.

Website is www.brightkettle.ie
Email is info@brightkettle.ie
Logo uploaded

I have ordered Business Card Printing via Print Harbor, the Double-sided colour printed option with gloss finish.

Industry/Entity Type

Business

```html
<!DOCTYPE html>
<html lang="en">
<head>
<meta charset="utf-8">
<title>Bright Kettle Business Card</title>
<link rel="stylesheet" href="https://fonts.googleapis.com/css2?family=Nunito:wght@900&family=PT+Sans&family=Tinos&display=swap">
<style>
  :root {
    --page-bg: #ececec;
    --card-back: #d6d6d6;
    --card-front: #ffffff;
    --ink: #111111;
    --brand-red: #c8101a;
    --label-ink: #1a1a1a;
  }
  * { margin: 0; padding: 0; box-sizing: border-box; }
  html, body { width: 1200px; height: 1000px; overflow: hidden; }
  body { background: var(--page-bg); position: relative; font-family: "Tinos", serif; }

  .panel-label {
    position: absolute; left: 60px; top: 150px;
    font-family: "PT Sans", sans-serif; font-size: 34px; line-height: 1.1;
    color: var(--label-ink);
  }

  .card {
    position: absolute; width: 500px; height: 286px;
    box-shadow: 0 6px 18px rgba(0,0,0,0.18);
    display: flex; flex-direction: column; align-items: center; justify-content: center;
  }
  .card--back { left: 70px; top: 380px; background: var(--card-back); }
  .card--front { left: 630px; top: 380px; background: var(--card-front); }

  .wordmark {
    display: flex; align-items: center; gap: 14px;
  }
  .wordmark__dot {
    width: 38px; height: 38px; border-radius: 50%; background: var(--brand-red);
  }
  .wordmark__name {
    font-family: "Nunito", sans-serif; font-weight: 900; font-size: 44px;
    color: var(--ink); letter-spacing: 0.5px;
  }

  .contact { font-size: 20px; color: var(--ink); }
  .contact--email { margin-bottom: 34px; }
  .contact--web { margin-top: 34px; font-size: 22px; }
</style>
</head>
<body>
  <div class="panel-label">Business Card<br>front &amp; back panel</div>

  <section class="card card--back">
    <div class="wordmark">
      <span class="wordmark__dot"></span>
      <span class="wordmark__name">BRIGHTKETTLE.IE</span>
    </div>
  </section>

  <section class="card card--front">
    <p class="contact contact--email">info@brightkettle.ie</p>
    <div class="wordmark">
      <span class="wordmark__dot"></span>
      <span class="wordmark__name">BRIGHTKETTLE.IE</span>
    </div>
    <p class="contact contact--web">www.brightkettle.ie</p>
  </section>
</body>
</html>
```